Velvet Paw Hospital Business Card Design

I need a business card designed for my cat only veterinary clinic. I will upload the logo that I would like included on the card. Please include:
Business Name: The Velvet Paw Hospital
Address: 20947 E. 38th St, Scottsdale, AZ 85371
Phone #: 480-555-6143
Website URL: www.velvetpawvets.com
And the Doctors Name: Marisol Brenn, DVM

```html
<!DOCTYPE html>
<html lang="en">
<head>
<meta charset="UTF-8">
<title>The Velvet Paw Hospital – Business Card</title>
<link rel="stylesheet" href="https://fonts.googleapis.com/css2?family=Poppins:wght@400;600&display=swap">
<style>
  :root {
    --page-bg: #e9e6e7;
    --card-top-light: #fbf8f8;
    --card-top-tint: #efe4e5;
    --accent-green: #62b845;
    --brand-purple: #813a86;
    --ink-dark: #111111;
    --ink-light: #ffffff;
    --mark-fill: #1f1a33;
  }
  * { margin: 0; padding: 0; box-sizing: border-box; }
  html, body {
    width: 1200px;
    height: 900px;
    overflow: hidden;
    background: var(--page-bg);
    font-family: "Poppins", sans-serif;
  }
  .business-card {
    position: absolute;
    left: 100px;
    top: 141px;
    width: 1000px;
    height: 618px;
    overflow: hidden;
    box-shadow: 0 10px 30px rgba(0, 0, 0, 0.18);
  }
  .card-header {
    position: absolute;
    left: 0; top: 0;
    width: 100%;
    height: 334px;
    background: radial-gradient(ellipse at 60% 45%, var(--card-top-light) 0%, var(--card-top-tint) 100%);
  }
  .brand-circle {
    position: absolute;
    left: 166px;
    top: 60px;
    width: 243px;
    height: 243px;
    border-radius: 50%;
    background: radial-gradient(circle at 50% 40%, #2c2550 0%, var(--mark-fill) 70%);
  }
  .brand-name {
    position: absolute;
    left: 426px;
    top: 128px;
    font-size: 56px;
    font-weight: 400;
    line-height: 60px;
    letter-spacing: 2px;
    color: var(--ink-dark);
  }
  .accent-rule {
    position: absolute;
    left: 0; top: 334px;
    width: 100%;
    height: 7px;
    background: var(--accent-green);
  }
  .card-footer {
    position: absolute;
    left: 0; top: 341px;
    width: 100%;
    height: 277px;
    background: var(--brand-purple);
    color: var(--ink-light);
  }
  .doctor-name {
    position: absolute;
    left: 85px;
    top: 75px;
    font-size: 36px;
    font-weight: 600;
    line-height: 50px;
    white-space: nowrap;
  }
  .divider {
    position: absolute;
    left: 511px;
    top: 53px;
    width: 2px;
    height: 94px;
    background: var(--ink-light);
  }
  .contact-list {
    position: absolute;
    left: 543px;
    top: 62px;
    list-style: none;
    font-size: 30px;
    line-height: 37px;
  }
  .contact-item {
    display: flex;
    align-items: center;
    white-space: nowrap;
  }
  .contact-icon {
    width: 28px;
    height: 28px;
    margin-right: 20px;
    flex: none;
  }
  .address {
    position: absolute;
    left: 0;
    width: 100%;
    top: 175px;
    text-align: center;
    font-size: 30px;
    line-height: 40px;
    white-space: nowrap;
  }
</style>
</head>
<body>
  <div class="business-card">
    <header class="card-header">
      <div class="brand-circle"></div>
      <div class="brand-name">The Velvet Paw<br>Hospital</div>
    </header>
    <div class="accent-rule"></div>
    <section class="card-footer">
      <div class="doctor-name">MARISOL BRENN, DVM</div>
      <div class="divider"></div>
      <ul class="contact-list">
        <li class="contact-item">
          <svg class="contact-icon" viewBox="0 0 24 24" fill="none" stroke="#ffffff" stroke-width="2" stroke-linecap="round" stroke-linejoin="round" aria-hidden="true">
            <path d="M5 3h3l2 5-2.5 1.5a11 11 0 0 0 7 7L16 14l5 2v3a2 2 0 0 1-2 2A16 16 0 0 1 3 5a2 2 0 0 1 2-2z"/>
            <path d="M15 3a6 6 0 0 1 6 6"/>
            <path d="M15 7a2 2 0 0 1 2 2"/>
          </svg>
          <span>480-555-6143</span>
        </li>
        <li class="contact-item">
          <svg class="contact-icon" viewBox="0 0 24 24" fill="none" stroke="#ffffff" stroke-width="1.8" aria-hidden="true">
            <circle cx="12" cy="12" r="9.5"/>
            <ellipse cx="12" cy="12" rx="4" ry="9.5"/>
            <path d="M2.5 12h19M4 7h16M4 17h16"/>
          </svg>
          <span>www.velvetpawvets.com</span>
        </li>
      </ul>
      <p class="address">20947 E. 38th St,&nbsp; Scottsdale, AZ 85371</p>
    </section>
  </div>
</body>
</html>
```